Oral Restoration Planners Guild Yearly Summit 2016 Flyer

We need a two page attention grabbing flyer promoting our upcoming conference in Dallas, TX at the Brindlewood Inn on August 27th and 28th 2016. The flyer should give information about the conference and what you will learn by attending and to accept registration through an Ticketvale link. Our mission is to define, educate and support the role of the dental implant coordinator. Bringing together like-minded professionals to network, practice share and define our role in the delivery of comprehensive patient care. 2 day annual conference open to Surgical implant coordinators and their surgeons

Target Market(s)

Surgical Implant Treatment Coordinators, their surgeons, and surgical team members

Industry/Entity Type

Dental

Requirements
Must have
• The ability for me to make changes.
Nice to have
• professional, eye catching,

```html
<!DOCTYPE html>
<html lang="en">
<head>
<meta charset="utf-8">
<title>Oral Restoration Planners Guild Yearly Summit 2016 Flyer</title>
<link href="https://fonts.googleapis.com/css2?family=Open+Sans:ital,wght@0,400;0,600;0,700;0,800;1,400&display=swap" rel="stylesheet">
<style>
  :root {
    --stage: #3a2b24;
    --paper: #ffffff;
    --ink: #111111;
    --brand-blue: #0f76bb;
    --swoosh-gray: #939598;
    --muted: #7a7a7a;
    --photo-a: #dfe8ee;
    --photo-b: #9fc9e2;
  }
  html, body {
    margin: 0;
    width: 1200px;
    height: 1200px;
    overflow: hidden;
    background: var(--stage);
    font-family: "Open Sans", Arial, sans-serif;
  }
  .flyer {
    position: absolute;
    left: 158px;
    top: 40px;
    width: 1092px;
    height: 1415px;
    background: var(--paper);
    transform: scale(0.8);
    transform-origin: 0 0;
    overflow: hidden;
  }
  .hero-photo {
    position: absolute;
    left: 400px;
    top: 80px;
    width: 692px;
    height: 780px;
    background: radial-gradient(ellipse at 55% 40%, var(--photo-a), var(--photo-b) 80%, var(--paper));
    clip-path: polygon(0 170px, 385px 170px, 385px 0, 692px 0, 692px 780px, 0 780px);
  }
  .swoosh {
    position: absolute;
    left: 0;
    top: 0;
    width: 1092px;
    height: 1415px;
  }
  .org-line {
    position: absolute;
    left: 32px;
    top: 26px;
    margin: 0;
    font-size: 45px;
    font-weight: 600;
    color: var(--ink);
    letter-spacing: 0.5px;
  }
  .event-title {
    position: absolute;
    left: 30px;
    top: 76px;
    margin: 0;
    font-size: 78px;
    font-weight: 800;
    line-height: 1;
    color: var(--brand-blue);
  }
  .event-year {
    position: absolute;
    left: 30px;
    top: 144px;
    margin: 0;
    font-size: 72px;
    font-weight: 800;
    color: var(--ink);
  }
  .guild-mark {
    position: absolute;
    left: 30px;
    top: 330px;
    display: flex;
    align-items: center;
    gap: 14px;
    font-size: 30px;
    font-weight: 600;
    color: var(--brand-blue);
    width: 380px;
    line-height: 1.2;
  }
  .guild-mark .dot {
    flex: 0 0 44px;
    height: 44px;
    border-radius: 50%;
    background: var(--brand-blue);
  }
  .tagline {
    position: absolute;
    left: 38px;
    top: 526px;
    width: 385px;
    margin: 0;
    font-size: 27px;
    font-style: italic;
    line-height: 32.5px;
    color: var(--muted);
  }
  .tagline .accent { color: var(--brand-blue); }
  .audience {
    position: absolute;
    left: 38px;
    top: 972px;
    width: 1045px;
    margin: 0;
    font-size: 37px;
    font-style: italic;
    line-height: 45px;
    color: var(--paper);
  }
  .speakers {
    position: absolute;
    left: 38px;
    top: 1110px;
    width: 1018px;
    color: var(--paper);
  }
  .speakers h2 {
    margin: 0;
    font-size: 27px;
    font-weight: 600;
    line-height: 32px;
  }
  .speakers p {
    margin: 0;
    font-size: 20.5px;
    line-height: 25.6px;
    text-align: justify;
  }
  .speakers em { font-style: italic; }
  .event-date {
    position: absolute;
    left: 38px;
    top: 1348px;
    margin: 0;
    font-size: 33px;
    font-weight: 600;
    color: var(--ink);
  }
  .event-date sup { font-size: 20px; }
</style>
</head>
<body>
  <main class="flyer">
    <div class="hero-photo" role="img" aria-label="Photo of a smiling dental assistant in blue scrubs and a dentist in a white coat with a stethoscope"></div>

    <svg class="swoosh" viewBox="0 0 1092 1415" aria-hidden="true">
      <path d="M0,905 Q700,890 1092,240 L1092,1415 L0,1415 Z" fill="var(--swoosh-gray)"/>
      <path d="M0,911 Q760,895 1092,535 L1092,1415 L0,1415 Z" fill="var(--paper)"/>
      <path d="M0,920 Q780,905 1092,555 L1092,1320 L0,1320 Z" fill="var(--brand-blue)"/>
      <rect x="0" y="1320" width="1092" height="8" fill="var(--swoosh-gray)"/>
    </svg>

    <h1 class="org-line">ORAL RESTORATION PLANNERS GUILD</h1>
    <p class="event-title">ORPG SUMMIT</p>
    <p class="event-year">2016</p>

    <div class="guild-mark"><span class="dot"></span><span>Oral Restoration Planners Guild</span></div>

    <p class="tagline">Bringing together <span class="accent">like-minded professionals</span> to network, prac-tice share and define our role in the delivery of comprehensive patient care</p>

    <p class="audience">Conference open to Surgical Implant Treatment Coordinators and their surgeons</p>

    <section class="speakers">
      <h2>SPEAKERS</h2>
      <p><em>Dr. Ravindra Kholwani</em>, DDS, MSD, Prosthodontist “Healthy Implants from Start to Finish”, <em>Tamsin Rowell,</em> America’s Body Language Expert and contributor to Harborline Report, “The Body Language of Effective Communication”, <em>Dr. Gerald P. Hensley</em>, DDS, Professor of Surgery &amp; Chief, U of Lakeshore School of Medicine, Dept of OMS, “The Effective use of rhBMP in Implant Dentistry”, <em>Marla Quinlan</em>, Professional Speaker, Author and Conversation Coach, “Team Building, Communication, and Case Acceptance”</p>
    </section>

    <p class="event-date">Saturday 27<sup>th</sup> and Sunday 28<sup>th</sup> at The Brindlewood Inn Dallas, TX</p>
  </main>
</body>
</html>
```